New Business Card Design Project VORASTI-Italy

we are VORASTI-Italy
our company in the market for 3 years we are luxury cosmetic company and its about time for a facelift :)
i will like to have elegant luxurious and unique business card
that will give the person that get it a unique, luxurious and elegant impression
I'm VERY OPEN FOR NEW IDEAS , even duo i add a few files of things that i see on line and i like them

i add my logo as well
my website is VORASTI.COM
(if you would like to see the main style that we have)

Target Market(s)

adult that have money :)

Industry/Entity Type

Business

Contact Information for Business Card

Name - Paul Vorasti
Position - CEO and CO Founder
address - 4817 E Larkdale
telephone - 555-384-1962
email - paul@vorasti.com
fax - 555-384-1962
website - VORASTI.COM

Colors
000000
959595
fbee3e
ffffff

Requirements
Must have
• big logo in GOLD color
• elegant look
• impressive
Nice to have
• not must but maybe classy pattern background
• not must but maybe emblem
• maybe clear plastic business card
Should not have
• colors
• images

```html
<!DOCTYPE html>
<html lang="en">
<head>
<meta charset="utf-8">
<title>VORASTI Italy – Business Card</title>
<link rel="stylesheet" href="https://fonts.googleapis.com/css2?family=Cinzel:wght@400&family=Ubuntu:wght@400;500&display=swap">
<style>
  :root {
    --stage: #1b1b1b;
    --card-black: #141414;
    --card-black-soft: #262626;
    --gold: #d4b04a;
    --gold-light: #e8cc6a;
    --gold-deep: #b8902e;
    --ink-dark: #111111;
    --ornament-tone: #3a3a3a;
  }
  * { box-sizing: border-box; margin: 0; padding: 0; }
  html, body {
    width: 1200px;
    height: 1200px;
    overflow: hidden;
    background: var(--stage);
  }
  .stage {
    position: relative;
    width: 1200px;
    height: 1200px;
  }
  .card {
    position: absolute;
    top: 180px;
    width: 480px;
    height: 840px;
    overflow: hidden;
    background: radial-gradient(ellipse at 50% 35%, var(--card-black-soft), var(--card-black) 75%);
  }
  .card--front { left: 90px; }
  .card--back { left: 630px; }

  /* front */
  .front-band {
    position: absolute;
    left: 0; top: 0;
    width: 100%; height: 38px;
    background: linear-gradient(90deg, var(--gold-deep), var(--gold-light) 50%, var(--gold-deep));
  }
  .front-band-rule {
    position: absolute;
    left: 0; top: 46px;
    width: 100%; height: 3px;
    background: var(--gold);
  }
  .pattern-area {
    position: absolute;
    left: -60px; bottom: -220px;
    width: 600px; height: 600px;
    border-radius: 50%;
    background: radial-gradient(circle, transparent 38%, rgba(70,70,70,0.45) 52%, rgba(70,70,70,0.25) 70%, transparent 72%);
  }
  .brand-disc {
    position: absolute;
    left: 50%;
    border-radius: 50%;
    border: 3px solid var(--gold);
    transform: translateX(-50%);
  }
  .card--front .brand-disc { top: 150px; width: 184px; height: 184px; }
  .brand-name {
    position: absolute;
    left: 0; width: 100%;
    text-align: center;
    font-family: "Cinzel", serif;
    font-weight: 400;
    color: var(--gold);
    line-height: 1;
  }
  .card--front .brand-name.name { top: 372px; font-size: 80px; }
  .card--front .brand-name.place { top: 490px; font-size: 28px; }
  .brand-rule {
    position: absolute;
    height: 3px;
    background: var(--gold);
  }
  .card--front .brand-rule { left: 36px; width: 408px; top: 470px; }

  /* back */
  .back-top {
    position: absolute;
    left: 0; top: 0;
    width: 480px; height: 310px;
  }
  .person {
    position: absolute;
    left: 0; width: 100%;
    text-align: center;
    font-family: "Ubuntu", sans-serif;
    color: var(--ink-dark);
  }
  .person-name { top: 48px; font-size: 44px; font-weight: 500; letter-spacing: 0.5px; }
  .person-role { top: 106px; font-size: 21px; font-weight: 400; letter-spacing: 0.5px; }
  .card--back .brand-disc { top: 200px; width: 148px; height: 148px; }
  .card--back .brand-name.name { top: 368px; font-size: 64px; }
  .card--back .brand-name.place { top: 467px; font-size: 24px; }
  .card--back .brand-rule { left: 78px; width: 324px; top: 452px; height: 2px; }
  .contact-list {
    position: absolute;
    left: 140px; top: 548px;
    list-style: none;
  }
  .contact-item {
    display: flex;
    align-items: center;
    height: 49px;
    font-family: "Ubuntu", sans-serif;
    font-size: 20px;
    color: var(--gold);
  }
  .contact-icon {
    width: 22px; height: 22px;
    margin-right: 14px;
    flex: none;
  }
</style>
</head>
<body>
<main class="stage">

  <section class="card card--front" aria-label="Card front">
    <div class="front-band"></div>
    <div class="front-band-rule"></div>
    <div class="pattern-area" role="img" aria-label="Faint circular ornamental pattern"></div>
    <div class="brand-disc"></div>
    <div class="brand-name name">VORASTI</div>
    <div class="brand-rule"></div>
    <div class="brand-name place">ITALY</div>
  </section>

  <section class="card card--back" aria-label="Card back">
    <div class="pattern-area" role="img" aria-label="Faint circular ornamental pattern"></div>
    <svg class="back-top" viewBox="0 0 480 310" aria-hidden="true">
      <defs>
        <linearGradient id="goldSheen" x1="0" y1="0" x2="1" y2="1">
          <stop offset="0" stop-color="#b8902e"/>
          <stop offset="0.5" stop-color="#e8cc6a"/>
          <stop offset="1" stop-color="#c29a36"/>
        </linearGradient>
      </defs>
      <rect x="0" y="0" width="480" height="293" fill="url(#goldSheen)"/>
      <path d="M123 293 V279 A117 117 0 0 1 357 279 V293 Z" fill="#1a1a1a"/>
      <rect x="0" y="298" width="118" height="3" fill="#d4b04a"/>
      <rect x="362" y="298" width="118" height="3" fill="#d4b04a"/>
    </svg>
    <div class="person person-name">PAUL VORASTI</div>
    <div class="person person-role">Ceo and CO Founder</div>
    <div class="brand-disc"></div>
    <div class="brand-name name">VORASTI</div>
    <div class="brand-rule"></div>
    <div class="brand-name place">ITALY</div>

    <ul class="contact-list">
      <li class="contact-item">
        <svg class="contact-icon" viewBox="0 0 24 24" aria-hidden="true"><path d="M12 2a7 7 0 0 0-7 7c0 5 7 13 7 13s7-8 7-13a7 7 0 0 0-7-7zm0 9.5A2.5 2.5 0 1 1 12 6.5a2.5 2.5 0 0 1 0 5z" fill="#d4b04a"/></svg>
        4817 E Larkdale
      </li>
      <li class="contact-item">
        <svg class="contact-icon" viewBox="0 0 24 24" aria-hidden="true"><rect x="3" y="6" width="18" height="12" fill="#d4b04a"/><path d="M3 6l9 7 9-7" fill="none" stroke="#141414" stroke-width="1.6"/></svg>
        paul@vorasti.com
      </li>
      <li class="contact-item">
        <svg class="contact-icon" viewBox="0 0 24 24" aria-hidden="true"><path d="M6.6 10.8a15 15 0 0 0 6.6 6.6l2.2-2.2a1 1 0 0 1 1-.25 11.4 11.4 0 0 0 3.6.57 1 1 0 0 1 1 1V20a1 1 0 0 1-1 1A17 17 0 0 1 3 4a1 1 0 0 1 1-1h3.5a1 1 0 0 1 1 1c0 1.25.2 2.45.57 3.6a1 1 0 0 1-.25 1z" fill="#d4b04a"/></svg>
        555-384-1962
      </li>
      <li class="contact-item">
        <svg class="contact-icon" viewBox="0 0 24 24" aria-hidden="true"><rect x="7" y="3" width="10" height="6" fill="#d4b04a"/><rect x="3" y="10" width="18" height="9" rx="1" fill="#d4b04a"/><rect x="7" y="15" width="10" height="6" fill="#141414" stroke="#d4b04a" stroke-width="1.5"/></svg>
        555-384-1962
      </li>
      <li class="contact-item">
        <svg class="contact-icon" viewBox="0 0 24 24" aria-hidden="true"><circle cx="12" cy="12" r="9" fill="none" stroke="#d4b04a" stroke-width="2"/><ellipse cx="12" cy="12" rx="4" ry="9" fill="none" stroke="#d4b04a" stroke-width="1.6"/><path d="M3 12h18M5 7h14M5 17h14" stroke="#d4b04a" stroke-width="1.4"/></svg>
        vorasti.com
      </li>
    </ul>
  </section>

</main>
</body>
</html>
```